Modernize and improve usability of our webpage www.lerntausch-brolani.ch (4 languages, mostly static content)

Need to modernize and freshen up the webpages of our association: www.lerntausch-brolani.ch We offer apprenticeship exchanges within Switzerland and abroad. Young people can inform and enroll online. We do the matchmaking with work locations and organize logistics, stay overs etc.
The webpage needs to be in 4 languages (German, French, Italian and English). The main pages will be:
- Landing page: what we do, targeted to our apprentices / young people who enroll for the stages.
- Sup-Page: Registration form for interested apprentices to sign up for the program
- Sub-Page "Company", the firms who would like to send their apprentices on a internship and info on how to join the program
- Sub-Page "Host Family", private people who would be interested in hosting the apprentices (for free) during the stages. Find out about the reqiurements for the host families
- Sub-Page "About Us", who we are, executive team, board of director, our sponsor "Harmil Circle Switzerland"
- Footer: contact (E-Mail, Telephone, WhatsApp), Bank details (IBAN Number), Partnerlogo of Harmil-Circle (see uploaded jpg), Social-Media Links (Facebook, LinkedIn)

Target Market(s)

Young people looking for a "apprenticeship" stage within Switzerland or going from Switzerland abroad

Industry/Entity Type

Apprenticeships: cooks, builders, craftsman, office support, etc.

Number of Pages Required

5+ page

Font styles to use
Other font styles liked:
• Lato (sans serif)

Requirements
Must have
• use colors shown on uploaded PDF-Slides: Make the BLUE the MAIN color, the ORANGE as a secondary color
Nice to have
• Forms using e.g. google forms or survey-monkey forms (external links, no code). Matching & appealing visuals showing young apprentices (can use stock photos)

```html
<!DOCTYPE html>
<html lang="en">
<head>
<meta charset="utf-8">
<title>Brolani – Apprenticeship Exchange</title>
<link rel="stylesheet" href="https://fonts.googleapis.com/css2?family=Lato:wght@400;700;900&family=Tinos:wght@400;700&display=swap">
<style>
:root{
  --blue:#1f3f7c;
  --blue-deep:#16305f;
  --navy:#262f40;
  --slate:#3a4767;
  --orange:#ff6500;
  --orange-soft:#ffc9a3;
  --lavender:#efeef8;
  --grey-text:#8a8d96;
  --line:#d9dbe2;
  --white:#ffffff;
  --sans:'Lato',sans-serif;
  --serif:'Tinos',serif;
}
*{box-sizing:border-box;margin:0;padding:0}
html,body{width:1200px;height:4673px;overflow:hidden;background:#fff}
body{font-family:var(--sans);color:#333}
.page{position:relative;width:1200px;height:4673px;overflow:hidden}
.abs{position:absolute}
.serif{font-family:var(--serif);font-weight:400}

/* header */
.top-contact{position:absolute;top:18px;display:flex;align-items:center;gap:10px}
.top-contact .dot{width:28px;height:28px;border-radius:50%;background:var(--blue);display:flex;align-items:center;justify-content:center}
.top-contact b{display:block;font-size:11px;color:#222}
.top-contact span{font-size:9px;color:var(--grey-text)}
.logo{position:absolute;font-family:var(--sans);font-weight:700;color:var(--orange);letter-spacing:.5px}
.btn-book{position:absolute;left:880px;top:10px;width:183px;height:40px;border-radius:20px;background:var(--blue-deep);color:#fff;font-size:11px;font-weight:700;display:flex;align-items:center;justify-content:center}
.nav a{position:absolute;top:86px;font-size:11px;color:#333;text-decoration:none}
.nav-rule{position:absolute;left:705px;top:66px;width:358px;height:1px;background:var(--line)}

/* hero */
.hero{position:absolute;left:0;top:123px;width:1200px;height:770px}
.hero-kicker{position:absolute;left:87px;top:368px;color:#fff;font-size:14px;letter-spacing:3px;font-weight:700}
.hero-title{position:absolute;left:87px;top:408px;color:#fff;font-size:44px;font-weight:900}
.hero-rule{position:absolute;left:87px;top:493px;width:633px;height:2px;background:rgba(255,255,255,.8)}
.hero-text{position:absolute;left:90px;top:524px;width:620px;color:#fff;font-size:14px;font-weight:700;line-height:1.75}
.pill{position:absolute;height:38px;border-radius:19px;font-size:13px;font-weight:700;display:flex;align-items:center;justify-content:center;letter-spacing:.5px}
.divider-badge{position:absolute;width:60px;height:60px;border-radius:50%;background:#fff;box-shadow:0 4px 14px rgba(0,0,0,.15);display:flex;align-items:center;justify-content:center}

/* tabs */
.tabs{position:absolute;left:90px;top:962px;width:980px;height:54px;background:#eceef2;display:flex}
.tab{flex:1;display:flex;align-items:center;justify-content:center;font-size:17px;font-weight:700;color:var(--blue);border-right:1px solid #cfd3db}
.tab:last-child{border-right:0}
.tab.active{background:#fff;border-bottom:3px solid var(--orange)}

/* about */
.about-kicker{position:absolute;left:620px;top:1134px;font-size:17px;color:var(--blue)}
.about-title{position:absolute;left:620px;top:1160px;font-size:45px;line-height:1.2;color:var(--blue);width:520px}
.about-quote{position:absolute;left:622px;top:1287px;width:470px;border-left:2px solid var(--blue);padding:6px 0 6px 15px;font-size:12.5px;line-height:1.8;color:var(--grey-text)}
.about-text{position:absolute;left:620px;top:1372px;width:470px;font-size:12.5px;line-height:1.85;color:var(--grey-text)}
.btn-orange{position:absolute;background:var(--orange);color:#fff;font-weight:700;display:flex;align-items:center;justify-content:center;gap:10px;border-radius:3px}

/* sections */
.section-title{position:absolute;left:0;width:1200px;text-align:center;font-size:46px;color:var(--blue)}
.section-sub{position:absolute;left:0;width:1200px;text-align:center;font-size:13px;line-height:1.8;color:var(--grey-text)}
.services-bg{position:absolute;left:0;top:1670px;width:1200px;height:572px;background:var(--lavender)}
.svc-card{position:absolute;top:1907px;width:320px;height:268px;border-radius:6px}
.svc-card h3{position:absolute;left:0;top:68px;width:100%;text-align:center;color:#fff;font-family:var(--serif);font-weight:700;font-size:27px}
.svc-icon{position:absolute;top:1873px;width:68px;height:68px;border-radius:50%;background:#fff;box-shadow:0 3px 10px rgba(0,0,0,.1);display:flex;align-items:center;justify-content:center}

/* why */
.why-item{position:absolute;width:240px}
.why-item h4{font-family:var(--serif);font-weight:400;font-size:22px;color:var(--blue);margin-bottom:10px}
.why-item p{font-size:12.5px;line-height:1.8;color:var(--grey-text)}
.why-item.left{text-align:right}
.why-icon{position:absolute;width:84px;height:84px;border-radius:50%;background:var(--blue);border:4px solid #fff;box-shadow:0 0 0 2px var(--blue);display:flex;align-items:center;justify-content:center}

/* enroll */
.hours-box{position:absolute;left:93px;top:3170px;width:467px;height:235px;background:rgba(20,30,55,.72);border-left:4px solid var(--orange)}
.hours-row{position:absolute;left:38px;width:400px;display:flex;justify-content:space-between;color:#fff;font-size:14px}
.hours-row b{font-weight:700}
.form-card{position:absolute;left:613px;top:3000px;width:490px;height:500px;background:var(--lavender)}
.field{position:absolute;height:54px;background:#fff;border:1px solid #e4e3ee;font-size:13px;color:#888;padding-left:26px;display:flex;align-items:center}

/* reviews */
.review{position:absolute;top:3812px;width:320px;height:268px;background:#fff;box-shadow:0 4px 18px rgba(30,40,80,.1)}
.review .stars{position:absolute;left:26px;top:58px;color:var(--orange);font-size:16px;letter-spacing:3px}
.review p{position:absolute;left:26px;top:88px;width:275px;font-size:12.5px;line-height:1.85;color:var(--grey-text)}
.review h5{position:absolute;left:26px;top:192px;font-family:var(--serif);font-weight:400;font-size:21px;color:var(--blue)}
.review small{position:absolute;left:26px;top:222px;font-size:9px;color:#777;letter-spacing:.5px}
.review .qmark{position:absolute;right:30px;top:-20px;font-family:var(--serif);font-weight:700;font-size:110px;line-height:1;color:var(--orange-soft)}
.review .qmark.strong{color:var(--orange)}
.avatar{position:absolute;top:3776px;width:64px;height:64px;border-radius:50%;border:3px solid #fff;box-shadow:0 2px 8px rgba(0,0,0,.15)}

/* footer */
.footer-nav{position:absolute;top:4440px;left:0;width:1200px;display:flex;justify-content:center;gap:48px}
.footer-nav a{color:#fff;font-size:13px;font-weight:700;text-decoration:none}
.foot-contact{position:absolute;top:4533px;display:flex;align-items:center;gap:16px;color:#fff}
.foot-contact .ring{width:58px;height:58px;border-radius:50%;border:1.5px solid rgba(255,255,255,.7);display:flex;align-items:center;justify-content:center}
.foot-contact b{display:block;font-size:12px;font-weight:700}
.foot-contact span{font-size:11px;font-weight:700}
.bottom-bar{position:absolute;left:0;top:4619px;width:1200px;height:54px;background:var(--slate)}
.bottom-bar .copy{position:absolute;left:152px;top:19px;color:#fff;font-size:12px;font-weight:700}
.social{position:absolute;top:15px;width:24px;height:24px;border:1.5px solid #fff;border-radius:3px}
</style>
</head>
<body>
<div class="page">

  <!-- Header -->
  <div class="top-contact" style="left:123px">
    <div class="dot"><svg width="13" height="13" viewBox="0 0 24 24" fill="#fff"><path d="M6.6 10.8a15 15 0 0 0 6.6 6.6l2.2-2.2a1 1 0 0 1 1-.25 11.4 11.4 0 0 0 3.6.57 1 1 0 0 1 1 1V20a1 1 0 0 1-1 1A17 17 0 0 1 3 4a1 1 0 0 1 1-1h3.5a1 1 0 0 1 1 1c0 1.25.2 2.45.57 3.57a1 1 0 0 1-.25 1z"/></svg></div>
    <div><b>Call Us:</b><span>(123) 456-7890</span></div>
  </div>
  <div class="top-contact" style="left:281px">
    <div class="dot"><svg width="13" height="13" viewBox="0 0 24 24" fill="#fff"><path d="M3 5h18v14H3z" fill="none" stroke="#fff" stroke-width="2"/><path d="M3 5l9 7 9-7" fill="none" stroke="#fff" stroke-width="2"/></svg></div>
    <div><b>Email:</b><span>office@company.com</span></div>
  </div>
  <div class="logo" style="left:536px;top:42px;font-size:36px">brolani</div>
  <div class="btn-book">BOOK APPOINTMENT</div>
  <div class="nav-rule"></div>
  <nav class="nav">
    <a style="left:132px">Home</a><a style="left:245px">About Us</a><a style="left:395px">Services</a>
    <a style="left:713px">Apprentices</a><a style="left:840px">Companies</a><a style="left:965px">Host Families</a>
  </nav>

  <!-- Hero -->
  <div class="hero" role="img" aria-label="Photo of young professionals working together in an office, tinted blue">
    <svg width="1200" height="770" viewBox="0 0 1200 770">
      <defs>
        <linearGradient id="heroGrad" x1="0" y1="0" x2="1" y2="0">
          <stop offset="0" stop-color="#1d3466"/>
          <stop offset=".55" stop-color="#34508a"/>
          <stop offset="1" stop-color="#25407a"/>
        </linearGradient>
      </defs>
      <rect width="1200" height="770" fill="url(#heroGrad)"/>
      <path d="M0,667 Q600,840 1200,667 L1200,770 L0,770 Z" fill="#fff"/>
    </svg>
  </div>
  <div class="hero-kicker">APPRENTICESHIP EXCHANGE SERVICES</div>
  <div class="hero-title">Bridging Skills for the future</div>
  <div class="hero-rule"></div>
  <div class="hero-text">Lorem ipsum dolor sit amet, consectetur adipiscing elit et dolore conser tempor incididunt ut labore et dolore magna</div>
  <div class="pill" style="left:83px;top:612px;width:146px;background:var(--blue-deep);color:#fff">LEARN MORE</div>
  <div class="pill" style="left:239px;top:612px;width:181px;background:#fff;color:#1b2a4a">REQUEST QUOTE</div>

  <svg class="abs" style="left:230px;top:855px" width="740" height="40" viewBox="0 0 740 40">
    <path d="M5,5 Q370,55 735,5" fill="none" stroke="var(--orange)" stroke-width="4" stroke-linecap="round"/>
  </svg>
  <div class="divider-badge" style="left:570px;top:862px"><svg width="22" height="14" viewBox="0 0 22 14"><path d="M2 2l9 9 9-9" fill="none" stroke="var(--orange)" stroke-width="3.5" stroke-linecap="round" stroke-linejoin="round"/></svg></div>

  <!-- Tabs -->
  <div class="tabs">
    <div class="tab active">For Apprentices</div>
    <div class="tab">For Host Families</div>
    <div class="tab">For Companies</div>
  </div>

  <!-- About -->
  <svg class="abs" style="left:80px;top:1110px" width="480" height="480" viewBox="0 0 480 480" role="img" aria-label="Portrait photo of a young apprentice in a workshop">
    <defs>
      <radialGradient id="aboutGrad" cx=".5" cy=".45" r=".6">
        <stop offset="0" stop-color="#8e97a3"/>
        <stop offset="1" stop-color="#4b5668"/>
      </radialGradient>
    </defs>
    <path d="M40,215 A200,200 0 0 1 470,240" fill="none" stroke="#3c5c92" stroke-width="8"/>
    <path d="M470,240 A200,200 0 0 1 330,420" fill="none" stroke="#3c5c92" stroke-width="8"/>
    <circle cx="240" cy="245" r="225" fill="url(#aboutGrad)" stroke="#fff" stroke-width="4"/>
  </svg>
  <div class="about-kicker serif">Strength in Apprenticeship Exchange</div>
  <div class="about-title serif">Skills Shared, Success Multiplied</div>
  <div class="about-quote">Lorem ipsum dolor sit amet, consectetur adipiscing elit, sed do eiusmod or incididunt ut labore et dolore</div>
  <div class="about-text">Lorem ipsum dolor sit amet, consectetur adipiscing elit, sed do eiusmod tem por incididunt ut labore et dolore magna aliqua. Ut enim ad minim veniam, quis nostrud exercitation ullamco laboris nisi ut aliquip ex ea commodo consequat. Duis aute irure dolor in reprehenderit in voluptate velit esse cillum dolore eu fugiat nulla pariatur. Excepteur</div>
  <div class="btn-orange" style="left:620px;top:1522px;width:155px;height:43px;font-size:13px">Contact us
    <svg width="16" height="12" viewBox="0 0 16 12"><path d="M0 6h14M9 1l5 5-5 5" fill="none" stroke="#fff" stroke-width="2"/></svg></div>

  <!-- Services -->
  <div class="services-bg"></div>
  <div class="section-title serif" style="top:1720px">Our Services</div>
  <div class="section-sub" style="top:1786px">Lorem ipsum dolor sit amet, consectetur adipiscing elit, sed do eiusmod temp<br>or incididunt ut labore et dolore</div>

  <div class="svc-card" style="left:91px;background:linear-gradient(160deg,#4a5f88,#27406f)" role="img" aria-label="Photo of two apprentices smiling together"><h3>Apprentice Matching</h3></div>
  <div class="svc-card" style="left:439px;background:linear-gradient(160deg,#59698a,#2d4473)" role="img" aria-label="Photo of people walking in a corridor"><h3>Industry Networking</h3></div>
  <div class="svc-card" style="left:786px;background:linear-gradient(160deg,#4f618a,#263f70)" role="img" aria-label="Photo of colleagues reviewing a tablet"><h3>Career Guidance</h3></div>

  <div class="svc-icon" style="left:136px"><svg width="30" height="30" viewBox="0 0 30 30" fill="none" stroke="var(--orange)" stroke-width="2.2"><path d="M4 26V18M10 26V13M16 26V16M22 26V9M4 14l7-6 5 4 9-8M21 4h4v4"/></svg></div>
  <div class="svc-icon" style="left:484px"><svg width="30" height="30" viewBox="0 0 30 30" fill="none" stroke="var(--orange)" stroke-width="2.2"><circle cx="15" cy="15" r="12"/><circle cx="15" cy="15" r="7"/><circle cx="15" cy="15" r="2.5" fill="var(--orange)"/></svg></div>
  <div class="svc-icon" style="left:831px"><svg width="30" height="30" viewBox="0 0 30 30" fill="none" stroke="var(--orange)" stroke-width="2.2"><circle cx="15" cy="9" r="5"/><path d="M8 27v-6a7 7 0 0 1 14 0v6M12 21h6"/></svg></div>

  <!-- Why choose us -->
  <div class="section-title serif" style="top:2296px">Why Choose Us</div>
  <div class="section-sub" style="top:2362px">Lorem ipsum dolor sit amet, consectetur adipiscing elit, sed do eiusmod temp<br>or incididunt ut labore et dolore</div>

  <svg class="abs" style="left:300px;top:2470px" width="600" height="440" viewBox="0 0 600 440">
    <defs>
      <linearGradient id="whyGlow" x1="0" y1="0" x2="1" y2="0">
        <stop offset="0" stop-color="#efeef8" stop-opacity="0"/>
        <stop offset=".3" stop-color="#e9e8f6"/>
        <stop offset=".7" stop-color="#e9e8f6"/>
        <stop offset="1" stop-color="#efeef8" stop-opacity="0"/>
      </linearGradient>
    </defs>
    <path d="M0,10 L180,10 A215,215 0 0 1 420,10 L600,10 L600,430 L420,430 A215,215 0 0 1 180,430 L0,430 Z" fill="url(#whyGlow)"/>
    <circle cx="300" cy="220" r="215" fill="#e2e1f3"/>
  </svg>
  <div class="abs" style="left:412px;top:2502px;width:376px;height:376px;border-radius:50%;background:linear-gradient(180deg,#5e6f93,#33466f)" role="img" aria-label="Portrait photo of a smiling businessman with arms crossed"></div>

  <div class="why-icon" style="left:400px;top:2519px"><svg width="34" height="34" viewBox="0 0 34 34" fill="none" stroke="#fff" stroke-width="2.4"><circle cx="17" cy="7" r="3"/><path d="M6 13h22M17 13v8l-6 9M17 21l6 9"/></svg></div>
  <div class="why-icon" style="left:400px;top:2652px"><svg width="34" height="34" viewBox="0 0 34 34" fill="none" stroke="#fff" stroke-width="2.6" stroke-linecap="round"><path d="M17 3v5M17 26v5M3 17h5M26 17h5M7 7l3.5 3.5M23.5 23.5L27 27M7 27l3.5-3.5M23.5 10.5L27 7"/></svg></div>
  <div class="why-icon" style="left:400px;top:2784px"><svg width="34" height="34" viewBox="0 0 34 34" fill="none" stroke="#fff" stroke-width="2.4"><path d="M8 18a9 9 0 0 1 18-2M26 16h-8M8 20h10M26 20a9 9 0 0 1-15 5"/></svg></div>
  <div class="why-icon" style="left:694px;top:2519px"><svg width="34" height="34" viewBox="0 0 34 34" fill="none" stroke="#fff" stroke-width="2.4"><circle cx="17" cy="17" r="12"/><circle cx="17" cy="17" r="6"/><circle cx="17" cy="17" r="2" fill="#fff"/></svg></div>
  <div class="why-icon" style="left:694px;top:2652px"><svg width="34" height="34" viewBox="0 0 34 34" fill="none" stroke="#fff" stroke-width="2.4"><path d="M8 18a9 9 0 0 1 18-2M26 16h-8M8 20h10M26 20a9 9 0 0 1-15 5"/></svg></div>
  <div class="why-icon" style="left:694px;top:2784px"><svg width="34" height="34" viewBox="0 0 34 34" fill="none" stroke="#fff" stroke-width="2.4"><rect x="5" y="6" width="6" height="6"/><rect x="23" y="6" width="6" height="6"/><rect x="5" y="22" width="6" height="6"/><rect x="23" y="22" width="6" height="6"/><path d="M11 9h12M11 25h12M8 12v10M26 12v10"/></svg></div>

  <div class="why-item left" style="left:135px;top:2517px"><h4>Tailored Solutions</h4><p>Lorem ipsum dolor sit amet, consectet ur adipiscing elit et dolore conser</p></div>
  <div class="why-item left" style="left:135px;top:2649px"><h4>Industry Connections</h4><p>Lorem ipsum dolor sit amet, consectet ur adipiscing elit et dolore conser</p></div>
  <div class="why-item left" style="left:135px;top:2782px"><h4>Global Perspective</h4><p>Lorem ipsum dolor sit amet, consectet ur adipiscing elit et dolore conser</p></div>
  <div class="why-item" style="left:797px;top:2517px"><h4>Skill Development</h4><p>Lorem ipsum dolor sit amet, consectet ur adipiscing elit et dolore conser</p></div>
  <div class="why-item" style="left:797px;top:2649px"><h4>Support System</h4><p>Lorem ipsum dolor sit amet, consectet ur adipiscing elit et dolore conser</p></div>
  <div class="why-item" style="left:797px;top:2782px"><h4>Connections</h4><p>Lorem ipsum dolor sit amet, consectet ur adipiscing elit et dolore conser</p></div>

  <!-- Enroll / opening hours -->
  <div class="abs" style="left:0;top:2977px;width:1200px;height:558px;background:linear-gradient(90deg,#1e3364 0%,#2e4678 55%,#4a5e8c 100%)" role="img" aria-label="Photo of people in an office hallway, tinted blue"></div>
  <div class="abs serif" style="left:93px;top:3108px;color:#fff;font-size:28px">Opening Hours</div>
  <div class="hours-box">
    <div class="hours-row" style="top:32px"><b>Monday - Friday</b><span>08am - 05pm</span></div>
    <div class="hours-row" style="top:82px"><b>Saturday</b><span>08am - 05pm</span></div>
    <div class="hours-row" style="top:134px"><b>Telephone</b><span>+123 456 7890</span></div>
    <div class="hours-row" style="top:184px"><b>Email</b><span>info@company.com</span></div>
  </div>

  <div class="form-card"></div>
  <div class="abs" style="left:667px;top:3040px;width:54px;height:54px;border-radius:50%;background:var(--blue);display:flex;align-items:center;justify-content:center"><svg width="24" height="24" viewBox="0 0 24 24" fill="none" stroke="#fff" stroke-width="1.8"><path d="M3 7h18v12H3z"/><path d="M3 7l9 7 9-7"/></svg></div>
  <div class="abs" style="left:733px;top:3040px;font-size:12.5px;font-weight:700;color:#222">Get in touch with us for more information</div>
  <div class="abs serif" style="left:746px;top:3062px;font-size:34px;color:var(--blue)">Enroll for Program</div>
  <div class="field" style="left:667px;top:3135px;width:182px">First Name</div>
  <div class="field" style="left:868px;top:3135px;width:183px">Last Name</div>
  <div class="field" style="left:667px;top:3207px;width:182px">Email Address</div>
  <div class="field" style="left:868px;top:3207px;width:183px">Phone Number</div>
  <div class="field" style="left:667px;top:3280px;width:384px">Select Subject</div>
  <div class="field" style="left:667px;top:3352px;width:384px">dd/mm/yyyy</div>
  <div class="btn-orange" style="left:667px;top:3425px;width:384px;height:53px;font-size:18px;border-radius:0">SUBMIT</div>

  <!-- Reviews -->
  <div class="section-title serif" style="top:3615px">Client Reviews</div>
  <div class="section-sub" style="top:3682px">Lorem ipsum dolor sit amet, consectetur adipiscing elit, sed do eiusmod temp<br>or incididunt ut labore et dolore</div>

  <div class="review" style="left:102px"><div class="qmark">”</div><div class="stars">★★★★★</div><p>Lorem ipsum dolor sit amet, consectetur adipiscing elit, sed do eiusmod tempor inci didunt ut labore et dolore magna aliqua. Ut enim ad minim veniam, quis</p><h5>Tara Redsing</h5><small>BUSINESSMAN</small></div>
  <div class="review" style="left:445px;border-bottom:4px solid var(--blue)"><div class="qmark strong">”</div><div class="stars">★★★★★</div><p>Lorem ipsum dolor sit amet, consectetur adipiscing elit, sed do eiusmod tempor inci didunt ut labore et dolore magna aliqua. Ut enim ad minim veniam, quis</p><h5>Tara Redsing</h5><small>BUSINESSMAN</small></div>
  <div class="review" style="left:789px"><div class="qmark">”</div><div class="stars">★★★★★</div><p>Lorem ipsum dolor sit amet, consectetur adipiscing elit, sed do eiusmod tempor inci didunt ut labore et dolore magna aliqua. Ut enim ad minim veniam, quis</p><h5>Tara Redsing</h5><small>BUSINESSMAN</small></div>
  <div class="avatar" style="left:130px;background:#d9b49a" role="img" aria-label="Client portrait"></div>
  <div class="avatar" style="left:473px;background:#c9c3be" role="img" aria-label="Client portrait"></div>
  <div class="avatar" style="left:817px;background:#bdbfc4" role="img" aria-label="Client portrait"></div>

  <!-- Footer -->
  <svg class="abs" style="left:0;top:4140px" width="1200" height="533" viewBox="0 0 1200 533">
    <path d="M0,12 Q600,150 1200,12 L1200,533 L0,533 Z" fill="var(--navy)"/>
    <path d="M235,70 Q600,125 965,70" fill="none" stroke="var(--orange)" stroke-width="4" stroke-linecap="round"/>
  </svg>
  <div class="divider-badge" style="left:570px;top:4206px"><svg width="22" height="14" viewBox="0 0 22 14"><path d="M2 2l9 9 9-9" fill="none" stroke="var(--orange)" stroke-width="3.5" stroke-linecap="round" stroke-linejoin="round"/></svg></div>
  <div class="logo" style="left:0;width:1200px;text-align:center;top:4330px;font-size:50px">brolani</div>
  <nav class="footer-nav"><a>HOME</a><a>SERVICES</a><a>ABOUT US</a><a>TESTIMONIALS</a><a>BLOG</a></nav>
  <div class="abs" style="left:142px;top:4495px;width:916px;height:1px;background:rgba(255,255,255,.5)"></div>

  <div class="foot-contact" style="left:172px">
    <div class="ring"><svg width="30" height="30" viewBox="0 0 30 30" fill="none" stroke="#fff" stroke-width="1.6"><circle cx="15" cy="15" r="12"/><path d="M3 15h24M15 3c-5 6-5 18 0 24M15 3c5 6 5 18 0 24"/></svg></div>
    <div><span>123, Building Name, Street<br>City, State XY 123456</span></div>
  </div>
  <div class="abs" style="left:430px;top:4530px;width:1px;height:64px;background:rgba(255,255,255,.6)"></div>
  <div class="foot-contact" style="left:503px">
    <div class="ring"><svg width="22" height="30" viewBox="0 0 22 30" fill="none" stroke="#fff" stroke-width="1.8"><rect x="4" y="3" width="14" height="24" rx="2"/><path d="M9 23h4"/></svg></div>
    <div><b>PHONE</b><span>(123) 456 7890</span></div>
  </div>
  <div class="abs" style="left:750px;top:4530px;width:1px;height:64px;background:rgba(255,255,255,.6)"></div>
  <div class="foot-contact" style="left:826px">
    <div class="ring"><svg width="28" height="28" viewBox="0 0 28 28" fill="none" stroke="#fff" stroke-width="1.8"><path d="M3 8h22v14H3z"/><path d="M3 8l11 8 11-8"/></svg></div>
    <div><b>EMAIL</b><span>info@company.com</span></div>
  </div>

  <div class="bottom-bar">
    <div class="copy">Brolani Apprenticeship exchange</div>
    <div class="social" style="left:935px"></div>
    <div class="social" style="left:968px"></div>
    <div class="social" style="left:1001px"></div>
    <div class="social" style="left:1034px"></div>
  </div>
</div>
</body>
</html>
```